Steel Company / Iron Railing Business Card Template

We are a custom steel fabrication company located in Trainer, PA. In business since 1979, we recently developed a new logo, and we're looking for a business card design to help display the new logo and our business. The name of the company is Kelbrook Forge Co.. The Office Phone number is (610) 555-0143. We fabricate and install custom "wrought iron" railings on our residential side, we also fabricate and erect structural steel (think cranes and steel beams in buildings) on our commercial side. Looking to get a business card template designed. Something modern, but professional. Clear and easy to read. Front should have all business and employee information including phone number(s), email address, business information, etc. back should spotlight logo.

Industry/Entity Type

Construction / Home Improvement

Contact Information for Business Card

Business information is Kelbrook Forge Co., 48 Dunmore Ave Suite 3305, Trainer, PA 19074. Phone number is (610) 555-0143. Website is www.kelbrookforge.example Business card should be for "Tom Pelling" with the job title "Sales & Estimating" but be editable for other employees. Tom's phone number is (610) 555-0178

Colors

Designer to choose colors to be used in the design.

Requirements
Must have
• Modern Feel, Design should be sized for standard business card sizing 3.5" x 2" (88.9mm x 50.8mm)

```html
<!DOCTYPE html>
<html lang="en">
<head>
<meta charset="utf-8">
<title>Kelbrook Forge Co. – Business Card</title>
<link href="https://fonts.googleapis.com/css2?family=Lexend:wght@300;400;600&display=swap" rel="stylesheet">
<style>
  :root {
    --backdrop: #9a9a9a;
    --card-dark: #252525;
    --emboss: #1a1a1a;
    --card-light: #ffffff;
    --rail-tint: #ececec;
    --brand-blue: #233f8f;
    --brand-red: #d0202a;
    --text-grey: #8a8a8a;
  }
  * { margin: 0; padding: 0; box-sizing: border-box; }
  html, body {
    width: 1200px; height: 1000px; overflow: hidden;
    background: var(--backdrop);
    font-family: "Lexend", sans-serif;
  }
  .card {
    position: absolute;
    left: 329px;
    width: 542px;
    height: 313px;
    border-radius: 29px;
    overflow: hidden;
  }
  .card--back {
    top: 187px;
    background: var(--card-dark);
    display: flex; align-items: center; justify-content: center;
  }
  .back-wordmark {
    color: var(--emboss);
    font-weight: 600;
    font-size: 38px;
    letter-spacing: 0.5px;
    display: flex; align-items: center; gap: 14px;
  }
  .back-wordmark .mark-dot {
    width: 26px; height: 26px; border-radius: 50%;
    background: var(--emboss);
  }
  .card--front {
    top: 539px;
    background: var(--card-light);
  }
  .railing-art {
    position: absolute; top: 0; left: 0;
    width: 542px; height: 313px;
  }
  .front-content {
    position: absolute; inset: 0;
    text-align: center;
  }
  .front-wordmark {
    position: absolute; top: 60px; left: 0; right: 0;
    color: var(--brand-blue);
    font-weight: 600;
    font-size: 24px;
  }
  .employee-name {
    position: absolute; top: 150px; left: 0; right: 0;
    color: var(--brand-blue);
    font-weight: 600; font-size: 16px; letter-spacing: 0.2px;
    line-height: 20px;
  }
  .employee-role {
    position: absolute; top: 170px; left: 0; right: 0;
    color: var(--brand-red);
    font-weight: 400; font-size: 17px; line-height: 20px;
  }
  .contact-list {
    position: absolute; top: 199px; left: 0; right: 0;
    list-style: none;
    font-size: 13.5px; font-weight: 300; line-height: 18px;
    color: var(--text-grey);
  }
  .contact-list .label { color: var(--brand-red); }
  .address {
    position: absolute; top: 285px; left: 0; right: 0;
    font-size: 12.5px; font-weight: 300;
    color: var(--text-grey);
  }
</style>
</head>
<body>
  <section class="card card--back">
    <div class="back-wordmark"><span class="mark-dot"></span>Kelbrook Forge Co.</div>
  </section>

  <section class="card card--front">
    <svg class="railing-art" viewBox="0 0 542 313" role="img" aria-label="Faint wrought iron railing illustration on both sides">
      <defs>
        <linearGradient id="rail-fade-left" x1="0" y1="0" x2="1" y2="0">
          <stop offset="0" stop-color="var(--rail-tint)" stop-opacity="1"/>
          <stop offset="0.6" stop-color="var(--rail-tint)" stop-opacity="0.7"/>
          <stop offset="1" stop-color="var(--rail-tint)" stop-opacity="0"/>
        </linearGradient>
        <linearGradient id="rail-fade-right" x1="1" y1="0" x2="0" y2="0">
          <stop offset="0" stop-color="var(--rail-tint)" stop-opacity="1"/>
          <stop offset="0.6" stop-color="var(--rail-tint)" stop-opacity="0.7"/>
          <stop offset="1" stop-color="var(--rail-tint)" stop-opacity="0"/>
        </linearGradient>
      </defs>
      <path d="M0 48 L156 128 Q160 150 150 160 L130 313 L0 313 Z" fill="url(#rail-fade-left)"/>
      <path d="M542 48 L386 128 Q382 150 392 160 L412 313 L542 313 Z" fill="url(#rail-fade-right)"/>
    </svg>
    <div class="front-content">
      <div class="front-wordmark">Kelbrook Forge Co.</div>
      <div class="employee-name">TOM PELLING</div>
      <div class="employee-role">Sales &amp; Estimating</div>
      <ul class="contact-list">
        <li><span class="label">m:</span> (610) 555-0178</li>
        <li><span class="label">o:</span> (610) 555-0143</li>
        <li><span class="label">e:</span> info@kelbrookforge.example</li>
        <li><span class="label">w:</span> kelbrookforge.example</li>
      </ul>
      <div class="address">48 Dunmore Ave, Suite 3305, Trainer, PA 19074</div>
    </div>
  </section>
</body>
</html>
```